Wine business webpage
Italian fine wines
Project: Wine business webpage
Wine business webpage -
Creative Brief
Fine and Rare Italian wine merchant
Cantina del Sole specializes in the Italy's fine and rare wines. We have special relationships with many of the greatest estates and their distributors, and are able to pass on the benefits of those relationships to our customers. We would welcome the opportunity to put our passion and knowledge to work for you!
Dislike: homepage with loads of bottles of wine, e.g. http://www.vintageharborcellars.example/
Nature
natural wood
green - Terre Verte
earth tone
top
http://www.marlowecask.example/
http://www.grapeledgerhub.example/
http://www.vinoquay.example/

```html
<!DOCTYPE html>
<html lang="en">
<head>
<meta charset="utf-8">
<title>Cantina del Sole — Fine &amp; Rare Italian Wines</title>
<link href="https://fonts.googleapis.com/css2?family=Arimo:wght@400;700&family=Cinzel:wght@400;700&family=IM+Fell+English&display=swap" rel="stylesheet">
<style>
:root{
  --header-green:#3f5a2a;
  --header-green-dark:#2b4019;
  --wood-light:#c8a877;
  --wood-mid:#b28d5a;
  --wood-dark:#4a2c18;
  --wood-darker:#2e1a0e;
  --logo-red:#7a2a1a;
  --paper:#efe6cf;
  --paper-edge:#dccfae;
  --gold:#c99a3a;
  --gold-dark:#9a7025;
  --leaf:#a9c23a;
  --leaf-dark:#7f9626;
  --ink:#3b2a1c;
  --ink-soft:#5d4a36;
  --wine-red:#8a2b1e;
  --cream:#f6ecd2;
  --white:#ffffff;
}
*{margin:0;padding:0;box-sizing:border-box}
html,body{width:1200px;height:925px;overflow:hidden}
body{position:relative;font-family:"Arimo",Arial,sans-serif;color:var(--ink);
  background:linear-gradient(90deg,var(--wood-mid) 0%,var(--wood-light) 35%,var(--wood-light) 65%,var(--wood-mid) 100%)}
.abs{position:absolute}

/* header */
.site-header{left:0;top:0;width:1200px;height:137px;
  background:linear-gradient(180deg,var(--header-green) 0%,var(--header-green-dark) 100%);
  border-bottom:3px solid #1f2e12}
.utility-bar{left:540px;top:6px;display:flex;gap:22px;font-size:11px;color:var(--cream)}
.utility-bar span{display:flex;align-items:center;gap:6px}
.utility-bar i{display:inline-block;width:10px;height:10px;border-radius:50%;background:var(--gold)}
.brand{left:200px;top:0;width:200px;height:162px;background:var(--logo-red);
  transform:rotate(-4deg);transform-origin:top left;box-shadow:0 4px 10px rgba(0,0,0,.45);
  display:flex;flex-direction:column;align-items:center;justify-content:center;gap:10px;border:3px solid #9c4a33}
.brand .mark{width:44px;height:44px;border-radius:50%;background:var(--cream)}
.brand .name{font-family:"Cinzel",serif;font-size:22px;color:var(--cream);text-align:center;line-height:1.1}
.main-nav{left:525px;top:95px;display:flex;gap:6px}
.main-nav a{display:block;padding:8px 14px;font-family:"Arimo",sans-serif;font-size:14px;color:var(--cream);text-decoration:none}
.main-nav a.current{background:var(--logo-red);border-radius:3px 3px 0 0}

/* sidebar */
.search-box{left:195px;top:175px;width:260px;height:75px;background:linear-gradient(180deg,#d7a84a,var(--gold-dark));
  border-radius:3px;box-shadow:0 2px 4px rgba(0,0,0,.3);padding:10px 12px}
.panel-title{font-family:"Cinzel",serif;font-size:16px;color:var(--ink)}
.search-field{display:flex;margin-top:6px}
.search-field span{width:200px;height:18px;background:var(--white);border:1px solid #8a6a2a}
.search-field b{width:18px;height:18px;background:var(--logo-red);margin-left:3px}
.categories{left:195px;top:262px;width:260px;height:350px;background:var(--paper);border:1px solid var(--paper-edge);
  box-shadow:0 2px 5px rgba(0,0,0,.25);padding:14px 16px}
.categories .panel-title{display:flex;align-items:center;gap:8px;margin-bottom:8px;padding-bottom:6px;border-bottom:1px solid var(--paper-edge)}
.categories .panel-title i{width:12px;height:12px;background:var(--ink-soft);border-radius:50%}
.categories ul{list-style:none}
.categories li{font-size:11px;color:var(--ink);padding:5px 0 5px 14px;border-bottom:1px solid #ddd0b2;position:relative}
.categories li::before{content:"";position:absolute;left:2px;top:9px;border-left:5px solid var(--ink-soft);border-top:3px solid transparent;border-bottom:3px solid transparent}
.download-box{left:195px;top:625px;width:260px;height:75px;background:linear-gradient(180deg,#d7a84a,var(--gold-dark));
  border-radius:3px;box-shadow:0 2px 4px rgba(0,0,0,.3);display:flex;align-items:center;padding:0 18px;gap:20px}
.download-box .label{font-family:"Cinzel",serif;font-size:17px;line-height:1.1;color:var(--ink)}
.download-box .files{display:flex;gap:14px}
.download-box .files i{width:26px;height:28px;background:var(--paper);border:2px solid var(--ink-soft)}
.newsletter{left:205px;top:712px;width:250px;height:83px;background:linear-gradient(180deg,var(--leaf),var(--leaf-dark));
  border-radius:3px;box-shadow:0 2px 4px rgba(0,0,0,.3);padding:10px 12px}
.newsletter .title{display:flex;align-items:center;gap:8px;font-family:"IM Fell English",serif;font-size:15px;color:var(--ink)}
.newsletter .row{display:flex;margin-top:10px;gap:6px}
.newsletter .row span{width:178px;height:20px;background:var(--white);font-size:10px;color:#777;padding:3px 5px}
.newsletter .row b{font-size:10px;background:var(--ink);color:var(--cream);padding:4px 6px}

/* slider */
.feature{left:480px;top:142px;width:525px;height:283px;box-shadow:0 3px 8px rgba(0,0,0,.4)}
.feature-photo{position:absolute;inset:0;
  background:linear-gradient(180deg,#b9b6a6 0%,#c9c6b4 30%,#7f8a5a 45%,#56692f 65%,#3c4d22 100%)}
.feature h1{position:absolute;right:22px;top:20px;font-family:"Cinzel",serif;font-weight:400;font-size:34px;line-height:1.05;
  color:var(--wine-red);text-align:center}
.arrow{width:40px;height:40px;background:var(--leaf);display:flex;align-items:center;justify-content:center;top:258px;box-shadow:0 2px 3px rgba(0,0,0,.3)}
.arrow.prev{left:462px}
.arrow.next{left:975px}

/* content */
.welcome{left:480px;top:425px;width:525px;height:265px;background:var(--paper);padding:18px 22px;box-shadow:0 2px 5px rgba(0,0,0,.25)}
.welcome h2{font-family:"IM Fell English",serif;font-weight:400;font-size:20px;color:var(--ink);margin-bottom:10px}
.welcome p{font-size:11.5px;line-height:1.5;color:var(--ink-soft);margin-bottom:10px;text-align:justify}

.promo{top:705px;width:243px;height:85px;border:3px solid var(--paper);box-shadow:0 2px 5px rgba(0,0,0,.35);overflow:hidden}
.promo.arrivals{left:492px;background:linear-gradient(90deg,#1e130c,#4a3322 60%,#8a6444)}
.promo.pick{left:762px;background:linear-gradient(90deg,#2a2a2a,#6d5f4e 55%,#b9ab91)}
.promo h3{position:absolute;left:10px;top:8px;font-family:"IM Fell English",serif;font-weight:400;font-size:19px;color:var(--white)}

/* footer */
.site-footer{left:0;top:812px;width:1200px;height:113px;background:linear-gradient(180deg,var(--wood-dark),var(--wood-darker))}
.footer-links{left:215px;top:845px;font-size:11px;color:var(--cream)}
.copyright{left:215px;top:872px;font-size:11px;color:var(--cream)}
.social{top:852px;width:34px;height:34px;border-radius:50%;border:2px solid var(--paper-edge);background:#6b4a30}
.social.one{left:920px}
.social.two{left:970px}
</style>
</head>
<body>

<header class="site-header abs">
  <div class="utility-bar abs">
    <span>Welcome, (Guest)</span>
    <span><i></i>View Cart</span>
    <span><i></i>My Account</span>
    <span><i></i>Login</span>
    <span><i></i>Help</span>
  </div>
  <nav class="main-nav abs">
    <a class="current">Home</a><a>About Us</a><a>Our Wines</a><a>News</a><a>Contact Us</a>
  </nav>
</header>

<div class="brand abs">
  <span class="mark"></span>
  <span class="name">Cantina<br>del Sole</span>
</div>

<aside>
  <div class="search-box abs">
    <div class="panel-title">Search</div>
    <div class="search-field"><span></span><b></b></div>
  </div>

  <div class="categories abs">
    <div class="panel-title"><i></i>Our Categories</div>
    <ul>
      <li>Australian</li><li>Bordeaux</li><li>Burgundy</li><li>Cabernet</li><li>Champagne</li>
      <li>Chardonnay</li><li>Italian</li><li>Merlot</li><li>Other</li><li>Port</li><li>Shiraz</li>
    </ul>
  </div>

  <div class="download-box abs">
    <div class="label">Download<br>Inventory</div>
    <div class="files"><i></i><i></i></div>
  </div>

  <div class="newsletter abs">
    <div class="title">
      <svg width="20" height="14" viewBox="0 0 20 14"><rect x="0.5" y="0.5" width="19" height="13" fill="#f6ecd2" stroke="#3b2a1c"/><path d="M1 1 L10 8 L19 1" fill="none" stroke="#3b2a1c"/></svg>
      Subscribe Newsletter
    </div>
    <div class="row"><span>Enter email address...</span><b>Go</b></div>
  </div>
</aside>

<section class="feature abs">
  <div class="feature-photo" role="img" aria-label="Photograph of vineyard rows stretching to distant hills under a pale sky"></div>
  <h1>I gradi del<br>vino migliore</h1>
</section>
<div class="arrow prev abs"><svg width="16" height="16" viewBox="0 0 16 16"><path d="M10 3 L5 8 L10 13" fill="none" stroke="#3f5a2a" stroke-width="2.5"/></svg></div>
<div class="arrow next abs"><svg width="16" height="16" viewBox="0 0 16 16"><path d="M6 3 L11 8 L6 13" fill="none" stroke="#3f5a2a" stroke-width="2.5"/></svg></div>

<main class="welcome abs">
  <h2>Welcome to Cantina del Sole</h2>
  <p>Cantina del Sole brings you the finest and rarest wines of Italy, chosen with care from the estates we know best. Our long friendships with growers and their distributors let us offer bottles that seldom reach the open market, at prices that reward your trust. Whether you are building a cellar or seeking one special bottle, we will guide you.</p>
  <p>From the hills of Piedmont to the slopes of Etna, every wine in our list carries the story of its land. We taste each vintage ourselves, store it in ideal conditions and ship it with the same care. Ask us about allocations, older vintages and rare formats, and let our passion and knowledge work for you.</p>
</main>

<div class="promo arrivals abs" role="img" aria-label="Photograph of a wine bottle in warm low light">
  <h3>New Arrivals</h3>
</div>
<div class="promo pick abs" role="img" aria-label="Photograph of bottles resting in a wooden case">
  <h3>Pick of the Month</h3>
</div>

<footer class="site-footer abs"></footer>
<div class="footer-links abs">Home | About Us | Our Wines | Ordering | News | Contact Us</div>
<div class="copyright abs">Copyright © 2011, Cantina del Sole. All rights reserved.</div>
<span class="social one abs"></span>
<span class="social two abs"></span>

</body>
</html>
```